Lumo Quest - Main Menu - Re-Design

I want to have a refresh for this app's main menu. There are some different items on the menu depending on the language (English vs. Non-English) and version (Pro vs. Free). I have attached screenshots of the different conditions. This app is a collection of brain training games.

Need designs for light and dark mode. Need designs for both portrait and landscape mode.

Here is a link to the app in Vexo Shelf.
https://shelf.vexomarket.test/store/apps/details?id=tarnwick.lumoquest

Here is a link to the app in the Quorra App Depot.
https://apps.quorradepot.test/us/app/lumo-quest-brain-training/id573918204?ls=1&mt=8

```html
<!DOCTYPE html>
<html lang="en">
<head>
<meta charset="UTF-8">
<title>Lumo Quest – Main Menu</title>
<link rel="stylesheet" href="https://fonts.googleapis.com/css2?family=Poppins:wght@400;500;600&display=swap">
<style>
  :root {
    --bg: #19191b;
    --text: #ffffff;
    --text-soft: rgba(255, 255, 255, 0.84);
    --divider: #6b6b70;
    --card-games: #7ba6d0;
    --card-training: #b39ad7;
    --card-learning: #e78e94;
    --card-scores: #e5cb94;
    --card-schedule: #9aa3dd;
    --avatar-top: #7cb1e0;
    --avatar-bottom: #5a8fc4;
    --badge: #1d6fa3;
    --art-games-a: #4a5b8c;
    --art-games-b: #263052;
    --art-training-a: #ece7f0;
    --art-training-b: #9a6ad0;
    --art-learning-a: #fdf0f1;
    --art-learning-b: #f2b8bd;
    --art-scores-a: #ece9e2;
    --art-scores-b: #cfa961;
    --art-schedule-a: #f07a74;
    --art-schedule-b: #d94c4c;
  }
  * { box-sizing: border-box; margin: 0; padding: 0; }
  html, body {
    width: 686px;
    height: 1200px;
    overflow: hidden;
    background: var(--bg);
  }
  body {
    font-family: "Poppins", sans-serif;
    color: var(--text);
    position: relative;
  }
  .status-bar {
    position: absolute;
    top: 0; left: 0; right: 0;
    height: 52px;
    display: flex;
    align-items: center;
    justify-content: space-between;
    padding: 0 44px 0 78px;
  }
  .status-time { font-size: 16px; font-weight: 500; }
  .status-icons { display: flex; gap: 7px; align-items: center; }

  .header {
    position: absolute;
    top: 76px; left: 38px; right: 38px;
    height: 150px;
  }
  .greeting { font-size: 21px; font-weight: 400; color: var(--text-soft); line-height: 1.3; }
  .user-name { font-size: 32px; font-weight: 600; margin-top: 2px; line-height: 1.2; }
  .theme-toggle {
    position: absolute;
    top: 92px; left: 0;
    width: 76px; height: 34px;
    border: 2px solid var(--text);
    border-radius: 17px;
  }
  .theme-toggle-knob {
    position: absolute;
    top: 3px; right: 4px;
    width: 24px; height: 24px;
    border-radius: 50%;
    background: var(--text);
  }
  .avatar {
    position: absolute;
    top: 0; right: 0;
    width: 104px; height: 104px;
    border-radius: 50%;
    background: linear-gradient(160deg, var(--avatar-top), var(--avatar-bottom));
  }
  .settings-badge {
    position: absolute;
    top: 66px; right: 84px;
    width: 36px; height: 36px;
    border-radius: 50%;
    background: var(--badge);
    border: 3px solid var(--bg);
    display: flex; align-items: center; justify-content: center;
  }
  .divider {
    position: absolute;
    top: 226px; left: 38px; right: 38px;
    height: 2px;
    background: var(--divider);
  }

  .menu {
    position: absolute;
    top: 250px; left: 38px; right: 38px;
    display: flex;
    flex-direction: column;
    gap: 36px;
  }
  .menu-card {
    position: relative;
    height: 172px;
    border-radius: 16px;
    padding: 0 34px;
    display: flex;
    flex-direction: column;
    justify-content: center;
    color: var(--text);
    text-decoration: none;
  }
  .menu-card--games { background: var(--card-games); }
  .menu-card--training { background: var(--card-training); }
  .menu-card--learning { background: var(--card-learning); }
  .menu-card--scores { background: var(--card-scores); }
  .menu-card--schedule {
    background: var(--card-schedule);
    justify-content: flex-start;
    padding-top: 44px;
  }
  .menu-title {
    font-size: 36px;
    font-weight: 600;
    letter-spacing: 2.5px;
    line-height: 1.15;
    position: relative;
    z-index: 1;
  }
  .menu-subtitle {
    font-size: 18px;
    font-weight: 400;
    color: var(--text-soft);
    margin-top: 2px;
    position: relative;
    z-index: 1;
  }
  .menu-art {
    position: absolute;
    right: 28px; top: 50%;
    transform: translateY(-50%);
    width: 150px; height: 116px;
    border-radius: 24px;
  }
  .menu-art--games { background: linear-gradient(135deg, var(--art-games-a), var(--art-games-b)); }
  .menu-art--training { background: linear-gradient(135deg, var(--art-training-a), var(--art-training-b)); width: 110px; }
  .menu-art--learning { background: linear-gradient(135deg, var(--art-learning-a), var(--art-learning-b)); }
  .menu-art--scores { background: linear-gradient(135deg, var(--art-scores-a), var(--art-scores-b)); }
  .menu-art--schedule {
    background: linear-gradient(135deg, var(--art-schedule-a), var(--art-schedule-b));
    top: 34px; transform: none;
    width: 110px; height: 90px;
  }
</style>
</head>
<body>
  <div class="status-bar">
    <span class="status-time">9:41</span>
    <div class="status-icons">
      <svg width="20" height="12" viewBox="0 0 20 12" aria-hidden="true">
        <rect x="0" y="8" width="3.5" height="4" rx="1" fill="#fff"/>
        <rect x="5.5" y="5.5" width="3.5" height="6.5" rx="1" fill="#fff"/>
        <rect x="11" y="3" width="3.5" height="9" rx="1" fill="#fff"/>
        <rect x="16.5" y="0" width="3.5" height="12" rx="1" fill="#fff"/>
      </svg>
      <svg width="18" height="13" viewBox="0 0 18 13" aria-hidden="true">
        <path d="M1 4.5a11.5 11.5 0 0 1 16 0" stroke="#fff" stroke-width="2" fill="none" stroke-linecap="round"/>
        <path d="M4 7.7a7 7 0 0 1 10 0" stroke="#fff" stroke-width="2" fill="none" stroke-linecap="round"/>
        <circle cx="9" cy="11" r="1.8" fill="#fff"/>
      </svg>
      <svg width="26" height="12" viewBox="0 0 26 12" aria-hidden="true">
        <rect x="0.5" y="0.5" width="22" height="11" rx="3" stroke="#fff" stroke-opacity="0.5" fill="none"/>
        <rect x="2" y="2" width="19" height="8" rx="1.6" fill="#fff"/>
        <rect x="23.5" y="4" width="2" height="4" rx="1" fill="#fff" fill-opacity="0.5"/>
      </svg>
    </div>
  </div>

  <header class="header">
    <p class="greeting">Welcome back,</p>
    <p class="user-name">Guest</p>
    <div class="theme-toggle" role="switch" aria-checked="true" aria-label="Dark mode">
      <span class="theme-toggle-knob"></span>
    </div>
    <div class="avatar" role="img" aria-label="User avatar illustration"></div>
    <div class="settings-badge" aria-label="Settings">
      <svg width="20" height="20" viewBox="0 0 20 20" aria-hidden="true">
        <circle cx="10" cy="10" r="6" fill="none" stroke="#fff" stroke-width="3.4" stroke-dasharray="2.4 2.3"/>
        <circle cx="10" cy="10" r="5" fill="#fff"/>
        <circle cx="10" cy="10" r="2.2" fill="#1d6fa3"/>
      </svg>
    </div>
  </header>

  <div class="divider"></div>

  <nav class="menu">
    <a class="menu-card menu-card--games">
      <span class="menu-title">GAME LIST</span>
      <span class="menu-subtitle">Exercise your brain memory</span>
      <span class="menu-art menu-art--games" role="img" aria-label="Game controller and headphones illustration"></span>
    </a>
    <a class="menu-card menu-card--training">
      <span class="menu-title">TRAINING CENTRE</span>
      <span class="menu-subtitle">Exercise regularly</span>
      <span class="menu-art menu-art--training" role="img" aria-label="Clipboard with checklist illustration"></span>
    </a>
    <a class="menu-card menu-card--learning">
      <span class="menu-title">LEARNING</span>
      <span class="menu-subtitle">Find lots of learning</span>
      <span class="menu-art menu-art--learning" role="img" aria-label="Cloud and light bulbs illustration"></span>
    </a>
    <a class="menu-card menu-card--scores">
      <span class="menu-title">SCORES</span>
      <span class="menu-subtitle">Find the top score here</span>
      <span class="menu-art menu-art--scores" role="img" aria-label="Trophies on a podium illustration"></span>
    </a>
    <a class="menu-card menu-card--schedule">
      <span class="menu-title">SCHEDULE</span>
      <span class="menu-art menu-art--schedule" role="img" aria-label="Desk calendar illustration"></span>
    </a>
  </nav>
</body>
</html>
```